Business Cards for new orthopaedic surgery practice

My husband and I are starting our own orthopaedic surgery practice. We are looking for a business card that is uniform, but one will have my name/title and the other will have his. You can just create one design with my name on it for now. But when I choose your design as the winning design I will ask that you add another copy with his name/title.

We are looking for classy, simple, elite all in one. We like dark blues/a little gold/yellow. Something that goes with our logo. We want our logo incorporated. Here is all the info you need:
Business name: RV Spine & Vitality Center
Location: 38915 North Bramble Ave
Harrow Bay, FL 34510
Phone: 954-218-4630
Fax: 954-571-2846
Email: info@myrvspine.example

Names: Lucinda Ferrow, M.D.
Board Certified Hand and Upper Extremity Surgeon

Emeka Dlunga, M.D.
Board Certified Hip & Knee Replacement/General Orthopaedic Surgeon

Can decide what you want to put on the back. Maybe a slogan:
Built on Trust. Devoted to You

I am just going to upload our logo. The only thing is if we select you as the winning design, the location, and phone numbers may change. We will need your help to update that once fully solidified.

Industry/Entity Type

Medical

Contact Information for Business Card

Colors
0054AA
0677BA
7BADD7
CADEEF
E8F1F8
0094D4
00A9DD
6FCCEA
C7EBF8
E9F6FB

Requirements
Must have
• class, appeal,
Should not have
• We want to air on the side of masculine if we are looking at masculine vs. feminine feel. But we still want it classy, sophisticated, and something we will love

```html
<!DOCTYPE html>
<html lang="en">
<head>
<meta charset="utf-8">
<title>RV Spine &amp; Vitality Center — Business Card</title>
<link rel="stylesheet" href="https://fonts.googleapis.com/css2?family=Cinzel:wght@500;600&family=Poppins:wght@400;500;700&display=swap">
<style>
  :root {
    --navy: #1e2a52;
    --navy-soft: #2a3766;
    --gold: #c9a25a;
    --white: #ffffff;
    --stage: #d6d6d6;
  }
  * { box-sizing: border-box; margin: 0; padding: 0; }
  html, body {
    width: 1200px;
    height: 900px;
    overflow: hidden;
    background: var(--stage);
    font-family: "Poppins", sans-serif;
  }
  .sheet {
    position: relative;
    width: 1200px;
    height: 900px;
  }
  .card {
    position: absolute;
    left: 250px;
    width: 700px;
    height: 400px;
    border-radius: 28px;
    overflow: hidden;
    box-shadow: 0 6px 18px rgba(0,0,0,0.25);
  }

  /* Back of card */
  .card-back {
    top: 35px;
    background: var(--navy);
    color: var(--white);
  }
  .back-mark {
    position: absolute;
    left: 0; right: 0;
    top: 120px;
    display: flex;
    align-items: center;
    justify-content: center;
    gap: 14px;
  }
  .back-mark .dot {
    width: 22px; height: 22px;
    border-radius: 50%;
    background: var(--gold);
  }
  .back-mark .practice-name {
    font-weight: 500;
    font-size: 26px;
    letter-spacing: 0.5px;
    color: var(--white);
  }
  .slogan {
    position: absolute;
    left: 0; right: 0;
    bottom: 70px;
    text-align: center;
    font-weight: 700;
    font-size: 26px;
  }
  .slogan .accent { color: var(--gold); }

  /* Front of card */
  .card-front {
    top: 465px;
    background: var(--white);
    color: var(--navy);
  }
  .identity {
    position: absolute;
    left: 48px;
    top: 52px;
  }
  .doctor-name {
    font-family: "Cinzel", serif;
    font-weight: 600;
    font-size: 30px;
    letter-spacing: 1px;
    color: var(--navy);
  }
  .doctor-title {
    margin-top: 4px;
    font-size: 19px;
    line-height: 1.25;
    color: var(--gold);
  }
  .contacts {
    position: absolute;
    left: 48px;
    top: 200px;
    list-style: none;
  }
  .contacts li {
    display: flex;
    align-items: center;
    gap: 12px;
    font-size: 18px;
    line-height: 1.45;
  }
  .contacts svg { width: 18px; height: 18px; fill: var(--gold); flex: none; }
  .address {
    position: absolute;
    left: 48px;
    top: 306px;
    font-style: normal;
    font-size: 18px;
    line-height: 1.35;
  }
  .front-mark {
    position: absolute;
    right: 40px;
    top: 60px;
    width: 230px;
    display: flex;
    flex-direction: column;
    align-items: center;
    gap: 16px;
    text-align: center;
  }
  .front-mark .dot {
    width: 70px; height: 70px;
    border-radius: 50%;
    background: var(--navy);
  }
  .front-mark .practice-name {
    font-weight: 500;
    font-size: 24px;
    line-height: 1.25;
    color: var(--navy);
  }
</style>
</head>
<body>
<main class="sheet">

  <section class="card card-back" aria-label="Card back">
    <div class="back-mark">
      <span class="dot"></span>
      <span class="practice-name">RV Spine &amp; Vitality Center</span>
    </div>
    <p class="slogan">Built on Trust. <span class="accent">Devoted to You</span></p>
  </section>

  <section class="card card-front" aria-label="Card front">
    <div class="identity">
      <h1 class="doctor-name">Lucinda Ferrow, M.D.</h1>
      <p class="doctor-title">Board Certified Hand and<br>Upper Extremity Surgeon</p>
    </div>

    <ul class="contacts">
      <li>
        <svg viewBox="0 0 24 24" aria-hidden="true"><path d="M6.6 10.8a15 15 0 0 0 6.6 6.6l2.2-2.2a1 1 0 0 1 1-.25 11.4 11.4 0 0 0 3.6.57 1 1 0 0 1 1 1V20a1 1 0 0 1-1 1A17 17 0 0 1 3 4a1 1 0 0 1 1-1h3.5a1 1 0 0 1 1 1c0 1.25.2 2.450.57 3.57a1 1 0 0 1-.25 1z"/></svg>
        954-218-4630
      </li>
      <li>
        <svg viewBox="0 0 24 24" aria-hidden="true"><path d="M6 2h12v6H6zM4 9h16a2 2 0 0 1 2 2v6h-4v5H6v-5H2v-6a2 2 0 0 1 2-2zm4 8v3h8v-3z"/></svg>
        954-571-2846
      </li>
      <li>
        <svg viewBox="0 0 24 24" aria-hidden="true"><path d="M2 5h20v14H2zm2 2v.4l8 5.2 8-5.2V7z"/></svg>
        info@myrvspine.example
      </li>
    </ul>

    <address class="address">
      38915 North Bramble Ave<br>
      Harrow Bay, FL 34510
    </address>

    <div class="front-mark">
      <span class="dot"></span>
      <span class="practice-name">RV Spine &amp;<br>Vitality Center</span>
    </div>
  </section>

</main>
</body>
</html>
```